Business Card Design for Boutique Agriculture Consulting Practice

Develop a modern Business card design using uploaded logos . Using the color specs 6C344F rgb(108, 52, 79) The fonts are trajan pro and eurostile. The business owner is a woman and should have a hint of femininity. This is what is behind the naming of the company: Rock roads are synonymous with the rural US landscape, where the corn grows and the cattle graze or for Hollow Creek Consulting home. But don’t let the dust get in your eyes, rock roads have edge and are often the only path to a spectacular destination. To navigate them one must know where they are going, have the courage to take a new path and the willingness to adjust their plans to get there.
Target Market(s)
Marketing Professionals
Industry/Entity Type
Agriculture
Contact Information for Business Card
Marisella Duvane
Title: Founder and CEO
Address: 20847 Pellman Lane, Larkfield Prairie 66074
Email: md@hollowcreekadvisory.example
Phone: 428.615.2940
Website: www.hollowcreekadvisory.example
Font styles to use
Other font styles liked:
- trajan pro and eurostile
Requirements
Must have
- Please use the correct color specs. Logo color specs are 6C344F rgb(108, 52, 79) The fonts are trajan pro and eurostile. Name, email and phone be the most important information included on the card
Should not have
- additional graphics

```html
<!DOCTYPE html>
<html lang="en">
<head>
<meta charset="utf-8">
<title>Hollow Creek Consulting – Business Card</title>
<link rel="stylesheet" href="https://fonts.googleapis.com/css2?family=Cinzel:wght@400;600&family=Michroma&display=swap">
<style>
  :root {
    --plum: #6c344f;
    --plum-deep: #5e2c45;
    --paper: #ffffff;
    --ground: #e9e6e8;
  }
  * { box-sizing: border-box; margin: 0; padding: 0; }
  html, body { width: 1200px; height: 880px; overflow: hidden; }
  body { background: var(--ground); position: relative; }

  .card {
    position: absolute;
    width: 560px;
    height: 320px;
    border-radius: 18px;
    overflow: hidden;
    box-shadow: 0 10px 30px rgba(40, 20, 30, 0.18);
  }

  /* Front */
  .card-front { left: 80px; top: 110px; background: var(--plum); color: var(--paper); }
  .front-brand {
    position: absolute; left: 0; right: 0; top: 104px; text-align: center;
    font-family: "Cinzel", serif; font-weight: 600; font-size: 34px;
    letter-spacing: 2px; line-height: 1.15; color: var(--paper);
  }
  .front-brand span { display: block; font-size: 17px; letter-spacing: 8px; }
  .front-web {
    position: absolute; left: 0; right: 0; top: 236px; text-align: center;
    font-family: "Michroma", sans-serif; font-size: 10.5px; letter-spacing: 1px;
  }

  /* Back */
  .card-back { left: 560px; top: 450px; background: var(--paper); color: var(--plum); }
  .back-brand {
    position: absolute; right: 42px; top: 54px; text-align: center;
    font-family: "Cinzel", serif; font-weight: 600; font-size: 28px;
    letter-spacing: 1.5px; line-height: 1.15; color: var(--plum);
  }
  .back-brand span { display: block; font-size: 14px; letter-spacing: 7px; }

  .divider { position: absolute; left: 36px; right: 36px; top: 196px; height: 1px; background: var(--plum); }

  .person { position: absolute; left: 40px; top: 150px; }
  .person-name {
    font-family: "Cinzel", serif; font-weight: 600; font-size: 19px; letter-spacing: 1px;
  }
  .person-title { font-family: "Michroma", sans-serif; font-size: 10px; margin-top: 3px; }

  .address {
    position: absolute; right: 40px; top: 150px; text-align: right;
    font-family: "Michroma", sans-serif; font-size: 10px; line-height: 1.6;
  }

  .contact { position: absolute; left: 40px; top: 210px; list-style: none; }
  .contact li {
    display: flex; align-items: center; gap: 8px; margin-bottom: 6px;
    font-family: "Michroma", sans-serif; font-size: 10.5px;
  }
  .contact svg { width: 16px; height: 16px; flex: none; }

  .footer-band { position: absolute; left: 0; bottom: 0; width: 560px; height: 56px; }
  .back-web {
    position: absolute; right: 36px; bottom: 20px;
    font-family: "Michroma", sans-serif; font-size: 10px; color: var(--paper); letter-spacing: 0.5px;
  }
</style>
</head>
<body>

  <section class="card card-front" aria-label="Card front">
    <div class="front-brand">Hollow Creek<span>Consulting</span></div>
    <div class="front-web">www.hollowcreekadvisory.example</div>
  </section>

  <section class="card card-back" aria-label="Card back">
    <div class="back-brand">Hollow Creek<span>Consulting</span></div>

    <div class="person">
      <div class="person-name">Marisella Duvane</div>
      <div class="person-title">Founder and CEO</div>
    </div>

    <div class="address">20847 Pellman Lane<br>Larkfield Prairie 66074</div>

    <div class="divider"></div>

    <ul class="contact">
      <li>
        <svg viewBox="0 0 16 16" aria-hidden="true"><circle cx="8" cy="8" r="7.3" fill="none" stroke="#6c344f" stroke-width="1.2"/><rect x="5.5" y="3.8" width="5" height="8.4" rx="1" fill="none" stroke="#6c344f" stroke-width="1.1"/></svg>
        428.615.2940
      </li>
      <li>
        <svg viewBox="0 0 16 16" aria-hidden="true"><circle cx="8" cy="8" r="8" fill="#6c344f"/><rect x="4" y="5.2" width="8" height="5.6" fill="none" stroke="#fff" stroke-width="1"/><path d="M4 5.2 L8 8.4 L12 5.2" fill="none" stroke="#fff" stroke-width="1"/></svg>
        md@hollowcreekadvisory.example
      </li>
    </ul>

    <svg class="footer-band" viewBox="0 0 560 56" aria-hidden="true">
      <polygon points="0,42 238,42 256,0 560,0 560,56 0,56" fill="#6c344f"/>
      <polyline points="0,34 234,34 250,-4" fill="none" stroke="#6c344f" stroke-width="1.2"/>
    </svg>
    <div class="back-web">www.hollowcreekadvisory.example</div>
  </section>

</body>
</html>
```